Flyer-Design für Erziehungs- und Familienberatungsstellen
Zielgruppe
Wir sind 14 Erziehungs- und Familienberatungsstellen in Mainstadt, in unterschiedlicher Trägerschaft, mit gemeinsamer Homepage. Nun wünschen wir uns einen gemeinsamen Flyer, der auf unser Angebot aufmerksam macht und auf die Homepage hinweist. Zielgruppe sind Kinder, Jugendliche, Eltern, Familien und Fachkräfte aus Einrichtungen, mit denen wir zusammen arbeiten.
Aufgabenstellung
Wir wünschen uns eine zweiseitig bedruckte Karte im DIN-lang Format (99 mm × 210 mm). Dieser sollte einen Eyecatcher, das Logo, den Link zur Seite www.kbzplu.de (auf Vorder- und Rückseite) und die beigefügte Frankfurt Karte sowie den Text: '14 Erziehungs- und Familienberatungsstellen in Mainstadt. Beratung für Eltern, Kinder und Jugendliche durch pädagogische und psychologische Fachkräfte. Unser Angebot ist freiwillig, kostenfrei und vertraulich.' enthalten. Uns ist wichtig, dass zwischen der Überschrift '14 Erziehungsberatungsstellen...' und dem Text 'Beratung für...' optisch gut unterschieden wird. Die Farbgebung sollte sich dem Logo anpassen.

```html
<!DOCTYPE html>
<html lang="de">
<head>
<meta charset="utf-8">
<title>Flyer – Erziehungs- und Familienberatung</title>
<link rel="stylesheet" href="https://fonts.googleapis.com/css2?family=Open+Sans:wght@400;600;700&family=Arimo:wght@700&display=swap">
<style>
  :root {
    --orange: #f7993a;
    --orange-deep: #ec8f32;
    --green: #b6cf10;
    --brown: #7a4611;
    --brown-dark: #6a3b10;
    --paper: #ffffff;
    --paper-soft: #fbfbfb;
    --stage: #e8e8e8;
    --map: #e2e2ea;
  }
  * { box-sizing: border-box; margin: 0; padding: 0; }
  html, body { width: 849px; height: 1200px; overflow: hidden; }
  body {
    background: var(--stage);
    font-family: "Open Sans", Arial, sans-serif;
    position: relative;
  }
  .flyer {
    position: absolute;
    top: 218px;
    width: 360px;
    height: 763px;
    background: var(--paper-soft);
    box-shadow: 0 3px 10px rgba(0,0,0,.25);
    overflow: hidden;
  }
  .flyer--front { left: 43px; }
  .flyer--back { left: 446px; }

  .band { position: absolute; left: 0; width: 100%; }
  .band--top-orange { top: 0; height: 14px; background: var(--orange); }
  .band--bottom-green { bottom: 0; height: 13px; background: var(--green); }
  .band--bottom-orange { bottom: 0; height: 13px; background: var(--orange); }

  .hero-photo {
    position: absolute; left: 0; top: 14px; width: 100%; height: 255px;
    background: radial-gradient(circle at 45% 35%, #fbfff0 0%, #d9eba4 35%, #9cc84a 70%, #6fa22a 100%);
    border-bottom: 3px solid var(--orange);
  }
  .count-badge {
    position: absolute; left: 195px; top: 258px; width: 162px; height: 162px;
    border-radius: 50%; background: var(--orange-deep);
    color: #fff; text-align: center;
    box-shadow: 0 2px 6px rgba(0,0,0,.2);
  }
  .count-badge__number { display: block; font-weight: 700; font-size: 42px; line-height: 1; margin-top: 12px; }
  .count-badge__text { display: block; font-weight: 600; font-size: 15.5px; line-height: 20px; margin-top: 3px; }

  .headline {
    position: absolute; left: 28px; top: 330px;
    font-weight: 600; font-size: 24px; line-height: 30px; color: var(--brown);
  }
  .subline {
    position: absolute; left: 28px; top: 449px;
    font-weight: 600; font-size: 21px; line-height: 31px; color: var(--orange);
  }
  .info-label {
    position: absolute; left: 28px;
    font-weight: 600; font-size: 15px; color: var(--brown);
  }
  .flyer--front .info-label { top: 547px; }
  .flyer--back .info-label { top: 539px; left: 33px; }

  .url-band {
    position: absolute; left: 0; top: 571px; width: 100%; height: 48px;
    display: flex; align-items: center; justify-content: center;
    font-family: "Arimo", Verdana, sans-serif; font-weight: 700;
    font-size: 33px; letter-spacing: 1px; color: #fff;
  }
  .url-band--orange { background: var(--orange); }
  .url-band--green { background: var(--green); }

  .org-mark {
    position: absolute; left: 22px; top: 664px;
    display: flex; align-items: center; gap: 12px;
  }
  .org-mark__dot { width: 44px; height: 44px; border-radius: 50%; background: var(--orange); }
  .org-mark__name { font-weight: 700; font-size: 17px; line-height: 19px; color: var(--orange); }

  .back-header {
    position: absolute; left: 0; top: 0; width: 100%; height: 298px;
    border-bottom: 7px solid var(--green);
  }
  .map-card {
    position: absolute; left: 16px; top: 50px; width: 329px; height: 330px;
    background: var(--paper);
    box-shadow: 0 3px 8px rgba(0,0,0,.25);
    padding: 14px;
  }
  .map-card__area {
    width: 100%; height: 100%;
    background: radial-gradient(ellipse at 55% 50%, var(--map) 0%, #ececf1 60%, #f7f7f9 100%);
  }
  .offer {
    position: absolute; left: 32px; top: 458px;
    font-family: "Arimo", Arial, sans-serif; font-weight: 700;
    font-size: 21.5px; line-height: 31px; color: var(--brown-dark);
  }
</style>
</head>
<body>

  <section class="flyer flyer--front">
    <div class="band band--top-orange"></div>
    <div class="hero-photo" role="img" aria-label="Foto: offene Hände halten eine Papierkette aus Familienfiguren vor grünem Laub und Sonnenlicht"></div>

    <h2 class="headline">Beratung für<br>Eltern, Kinder<br>und Jugendliche</h2>

    <div class="count-badge">
      <span class="count-badge__number">14</span>
      <span class="count-badge__text">Erziehungs- und<br>Familienberatungs-<br>stellen in der<br>Mainstadt</span>
    </div>

    <p class="subline">durch pädagogische und<br>psychologische Fachkräfte</p>
    <p class="info-label">Für nähere Informationen:</p>
    <div class="url-band url-band--orange">www.kbzplu.de</div>

    <div class="org-mark">
      <span class="org-mark__dot"></span>
      <span class="org-mark__name">Familienrat Mainstadt</span>
    </div>
    <div class="band band--bottom-green"></div>
  </section>

  <section class="flyer flyer--back">
    <svg class="back-header" width="360" height="298" viewBox="0 0 360 298" aria-hidden="true">
      <rect width="360" height="298" fill="#f7993a"/>
      <polygon points="0,0 148,0 0,142" fill="#b6cf10"/>
    </svg>
    <div class="map-card">
      <div class="map-card__area" role="img" aria-label="Stadtkarte mit Flussverlauf und den markierten Standorten der 14 Beratungsstellen"></div>
    </div>

    <p class="offer">Unser Angebot ist freiwillig,<br>kostenfrei und vertraulich.</p>
    <p class="info-label">Für nähere Informationen:</p>
    <div class="url-band url-band--green">www.kbzplu.de</div>

    <div class="org-mark">
      <span class="org-mark__dot"></span>
      <span class="org-mark__name">Familienrat Mainstadt</span>
    </div>
    <div class="band band--bottom-orange"></div>
  </section>

</body>
</html>
```